Disability Support service provider Needs a shopfront graphic Design

We are based in Sydney, Australia. Our company is called 'Coral Step Care Services'. We provide care services to anyone with a disability. I would like to see designs that are colourful and perhaps transparent. The colours from my logo uploaded can be used as a guide. I would also like a bit of information about our services on the design somewhere maybe in point form, for eg. Disability Support Services, We are people helping People, take control of your disability, supporting people to live the life they want to live, I would like the design to be friendly and inviting.

```html
<!DOCTYPE html>
<html lang="en">
<head>
<meta charset="utf-8">
<title>Coral Step Care Services – Shopfront Banner</title>
<link rel="stylesheet" href="https://fonts.googleapis.com/css2?family=Cinzel:wght@600&family=Quicksand:wght@500&display=swap">
<style>
  :root {
    --canvas: #ffffff;
    --maroon: #6b3334;
    --blue: #6a87bd;
    --gold: #e5ae24;
    --leaf-green: #9fcd45;
    --circle-tint: #e3eaf5;
    --frame: #e6e6e6;
    --white: #ffffff;
  }
  html, body {
    margin: 0;
    padding: 0;
    width: 1200px;
    height: 1200px;
    overflow: hidden;
    background: var(--canvas);
  }
  .shopfront-banner {
    position: absolute;
    left: 42px;
    top: 242px;
    width: 1098px;
    height: 555px;
    border: 1px solid var(--frame);
    box-sizing: border-box;
    background: var(--white);
  }
  .shopfront-banner svg {
    display: block;
    width: 100%;
    height: 100%;
  }
  .brand-name {
    font-family: "Cinzel", serif;
    font-weight: 600;
    fill: var(--maroon);
  }
  .tagline {
    font-family: "Quicksand", sans-serif;
    font-weight: 500;
    font-size: 37px;
    fill: var(--blue);
  }
  .services {
    font-family: "Quicksand", sans-serif;
    font-weight: 500;
    font-size: 41px;
    fill: var(--white);
    letter-spacing: -0.5px;
  }
  .services .bullet { fill: var(--leaf-green); }
  .brand-dot { fill: var(--circle-tint); }
  .wave-gold { fill: var(--gold); }
  .wave-blue { fill: var(--blue); }
</style>
</head>
<body>
  <div class="shopfront-banner">
    <svg viewBox="0 0 1372 693" preserveAspectRatio="none" aria-label="Coral Step Care Services shopfront banner">
      <defs>
        <path id="tagline-curve" d="M100,478 C500,498 950,468 1300,300"/>
      </defs>

      <circle class="brand-dot" cx="197" cy="213" r="110"/>

      <text class="brand-name" x="367" y="228" font-size="104">CORAL STEP</text>
      <text class="brand-name" x="444" y="306" font-size="80">CARE SERVICES</text>

      <path class="wave-gold" d="M0,493 C300,530 850,540 1372,288 L1372,298 C850,558 300,556 0,524 Z"/>
      <path class="wave-blue" d="M0,530 C300,562 850,566 1372,304 L1372,693 L0,693 Z"/>

      <text class="tagline">
        <textPath href="#tagline-curve" textLength="1190" lengthAdjust="spacing">We are people helping People. Supporting the life you want to live</textPath>
      </text>

      <text class="services" x="686" y="603" text-anchor="middle">Travel <tspan class="bullet">•</tspan> Cleaning <tspan class="bullet">•</tspan> Accommodation <tspan class="bullet">•</tspan> Everyday household tasks</text>
      <text class="services" x="682" y="655" text-anchor="middle">provided for the elderly and people with a disability</text>
    </svg>
  </div>
</body>
</html>
```